全国の1人〜2人で営業されている理・美容室のオーナーさん方にコロナでも全く影響を受けてない当サロンのノウハウを読んで頂きたいと思っています。
これからのサロンのあり方、考え方、今すぐに取り入れるべき技術や商品、売り上げの上げ方などをお伝えします。本気で環境を変えたい方、美容師の仕事、接客、人をキレイにすることが大好きな方、意識の高いお客様に囲まれずっと通って頂けるような、そんな美容室を一緒に作って行きたいです。

この度はご提案、修正と本当にありがとうございました。最後の最後までかなり悩みました。
初めての電子書籍で良い表紙デザインと出会うことが出来ました。

今回、ご提案頂いた皆さん、本当にありがとうございました。初心者の自分に親身になって頂き、皆さんの丁寧なデザインに感動しました。また2冊目も考えています。ご縁があればまたよろしくお願いします。

```html
<!DOCTYPE html>
<html lang="ja">
<head>
<meta charset="utf-8">
<title>これからサロンが生き残る方法</title>
<link rel="stylesheet" href="https://fonts.googleapis.com/css2?family=Noto+Sans+JP:wght@500;700;900&display=swap">
<style>
  :root {
    --red: #e1312a;
    --ink: #141414;
    --white: #ffffff;
    --wood-light: #b07a4c;
    --wood-dark: #4a2a17;
    --cape: #1c1c1e;
    --skin: #d9a98a;
  }
  html, body {
    margin: 0;
    padding: 0;
    width: 750px;
    height: 1200px;
    overflow: hidden;
    background: var(--white);
  }
  .cover {
    position: relative;
    width: 750px;
    height: 1200px;
    overflow: hidden;
    font-family: "Noto Sans JP", sans-serif;
  }
  .cover-photo {
    position: absolute;
    inset: 0;
    background:
      radial-gradient(ellipse 36% 22% at 58% 62%, var(--skin) 0%, rgba(217,169,138,0) 100%),
      linear-gradient(180deg, rgba(28,28,30,0) 72%, var(--cape) 82%),
      linear-gradient(120deg, var(--wood-light) 0%, #8c5a34 45%, var(--wood-dark) 100%);
  }
  .side-band {
    position: absolute;
    left: 0;
    top: 0;
    width: 212px;
    height: 1200px;
    background: var(--red);
  }
  .vertical {
    position: absolute;
    writing-mode: vertical-rl;
    text-orientation: upright;
    white-space: nowrap;
    line-height: 1;
  }
  .lead {
    font-weight: 700;
    color: var(--ink);
    -webkit-text-stroke: 8px var(--white);
    paint-order: stroke fill;
  }
  .lead-count { left: 440px; top: 26px; font-size: 32px; letter-spacing: 1px; }
  .lead-audience { left: 400px; top: 110px; font-size: 35px; letter-spacing: 1px; }
  .subtitle {
    left: 322px; top: 86px;
    font-size: 44px;
    font-weight: 900;
    color: var(--red);
    -webkit-text-stroke: 9px var(--white);
    paint-order: stroke fill;
  }
  .title-main {
    left: 228px; top: 118px;
    font-size: 102px;
    font-weight: 900;
    color: var(--ink);
    -webkit-text-stroke: 12px var(--white);
    paint-order: stroke fill;
  }
  .title-band {
    left: 56px; top: 68px;
    font-size: 98px;
    font-weight: 900;
    color: var(--white);
    letter-spacing: 2px;
  }
  .author {
    left: 82px; top: 660px;
    font-size: 46px;
    font-weight: 500;
    color: var(--white);
    letter-spacing: 4px;
  }
  .author-rule {
    position: absolute;
    left: 60px;
    width: 92px;
    height: 2px;
    background: var(--white);
  }
  .author-rule.top { top: 632px; }
  .author-rule.bottom { top: 1010px; }
</style>
</head>
<body>
  <div class="cover">
    <div class="cover-photo" role="img" aria-label="理容室で散髪を受けて笑顔の男の子の写真"></div>
    <div class="side-band"></div>

    <div class="vertical lead lead-count">1、2人で営業されている</div>
    <div class="vertical lead lead-audience">理・美容室のオーナーへ</div>
    <div class="vertical subtitle">コロナや景気に左右されない、</div>
    <h1 class="vertical title-main" style="margin:0">これからサロンが</h1>
    <div class="vertical title-band">生き残る方法</div>

    <div class="author-rule top"></div>
    <div class="vertical author">やまもとけんじ</div>
    <div class="author-rule bottom"></div>
  </div>
</body>
</html>
```